Re-design a highly converting profile page for my website

My website allows people to book a mentor for long-term mentorship as well as sessions. I would like to re-design this site within our branding guidelines to give people the best profile possible.

Please give this website a modern look and concentrate on the CTA and conversion rates. This is a highly converting site and it should stay that way or even get better!

Please also keep menu bar & footer in tact

Target Market(s)

Developers, Designers, Entrepreneurs in the Tech industry

Number of Pages Required

1 page

Requirements
Must have
• Strong CTA, existing color palette, testimonials and major elements
Nice to have
• Modern look, easy to see CTA, easy to scan offer. Not too crowded
Should not have
• No reporpusing. It is and stays a profile page

```html
<!DOCTYPE html>
<html lang="en">
<head>
<meta charset="utf-8">
<title>Owen Carrow – Mentor Profile</title>
<link href="https://fonts.googleapis.com/css2?family=Inter:ital,wght@0,400;0,500;0,600;0,700;1,400&display=swap" rel="stylesheet">
<style>
:root{
  --navy:#2e3e5d;
  --mint:#d4f8ef;
  --mint-text:#2f9275;
  --grey:#8a94a6;
  --body:#3a3f4a;
  --star:#f7931e;
  --border:#d6dee8;
  --tag:#f1f2f4;
  --footer:#e5eaf1;
  --white:#ffffff;
}
*{box-sizing:border-box;margin:0;padding:0}
html,body{width:1200px;height:2667px;overflow:hidden;background:var(--white)}
body{position:relative;font-family:"Inter",sans-serif;color:var(--body)}
.abs{position:absolute}
a{color:inherit;text-decoration:none}

/* nav */
.brand-dot{left:83px;top:23px;width:37px;height:37px;border-radius:50%;background:var(--navy)}
.nav-link{top:32px;font-size:15px;font-weight:500;color:var(--navy)}
.btn-login{left:876px;top:24px;width:90px;height:35px;background:var(--mint);color:var(--mint-text);font-size:15px;font-weight:500;display:flex;align-items:center;justify-content:center}
.btn-start{left:983px;top:24px;width:134px;height:35px;background:var(--navy);color:var(--white);font-size:15px;font-weight:500;display:flex;align-items:center;justify-content:center}

/* hero */
.avatar-lg{left:82px;top:133px;width:208px;height:208px;border-radius:50%;background:radial-gradient(circle at 50% 40%,#d9a88c,#b86a6a 60%,#cfc7bd)}
.social{top:362px;font-size:14px;font-weight:600;color:#1a8ad0}
.mentor-name{left:320px;top:182px;font-size:38px;font-weight:700;color:var(--navy);letter-spacing:-.3px}
.mentor-role{left:322px;top:238px;font-size:17px;color:var(--grey)}
.stars{color:var(--star);letter-spacing:4px}
.hero-stars{left:322px;top:266px;font-size:25px}
.review-count{left:471px;top:271px;font-size:18px;font-style:italic;color:var(--grey)}
.price{left:828px;top:177px;font-size:38px;font-weight:600;color:var(--grey)}
.btn-apply{left:828px;top:238px;width:289px;height:54px;background:var(--navy);color:var(--white);font-size:25px;font-weight:500;display:flex;align-items:center;justify-content:center}
.spots{right:83px;top:297px;font-size:14px;font-weight:500;color:var(--grey)}

/* sections */
.section-title{font-size:24px;font-weight:600;color:#1d2230}
.tags{left:109px;top:554px;width:620px;display:flex;flex-wrap:wrap;gap:14px 13px}
.tag{height:36px;padding:0 20px;background:var(--tag);font-size:12px;font-weight:600;color:#222;display:flex;align-items:center;border-radius:2px}
.tag.active{background:var(--mint);color:var(--mint-text);font-weight:500}
.para{left:109px;width:626px;font-size:13.4px;line-height:20px;color:var(--body)}
.para a{color:#2a9fd0}
.bullets{left:109px;top:1100px;list-style:none;font-size:13.4px}
.bullets li{height:40px}

.testi-avatar{width:54px;height:54px;border-radius:50%}
.testi-name{left:177px;font-size:21px;color:#1d2230}
.testi-stars{left:177px;font-size:18px;letter-spacing:3px}
.testi-text{left:177px;width:556px;font-size:13.4px;line-height:20px;color:#2a2e38}
.more-reviews{left:357px;top:1769px;font-size:15px;color:var(--mint-text)}

/* sidebar */
.card{border:2px solid var(--border);border-radius:2px}
.book-card{left:790px;top:473px;width:327px;height:639px}
.session-name{left:825px;font-size:15px;font-weight:600;color:#1d2230}
.session-meta{left:825px;font-size:13.5px;color:var(--grey)}
.btn-book{left:825px;width:134px;height:36px;background:var(--navy);color:var(--white);font-size:15px;font-weight:500;display:flex;align-items:center;justify-content:center}
.divider{left:810px;width:287px;height:2px;background:var(--border)}
.btn-more{left:810px;top:1031px;width:287px;height:49px;background:var(--mint);color:var(--mint-text);font-size:19px;font-weight:500;display:flex;align-items:center;justify-content:center}
.related-card{left:790px;top:1156px;width:327px;height:508px}
.rel-avatar{left:809px;width:54px;height:54px;border-radius:50%}
.rel-name{left:873px;font-size:19px;font-weight:600;color:#1d2230}
.rel-role{left:873px;width:150px;font-size:11.5px;line-height:14px;color:var(--grey)}
.rel-price{left:1032px;font-size:15px;line-height:19px;font-weight:500;color:#1d2230}
.rel-price span{display:block;padding-left:13px}

/* cta band */
.cta-band{left:0;top:1862px;width:1200px;height:346px;background:var(--navy)}
.cta-heading{left:0;top:1940px;width:1200px;text-align:center;font-size:37px;line-height:43px;font-weight:700;letter-spacing:3px;color:var(--white)}
.btn-cta{left:455px;top:2071px;width:289px;height:54px;background:var(--white);color:var(--navy);font-size:25px;font-weight:500;display:flex;align-items:center;justify-content:center}

/* footer */
.footer{left:0;top:2208px;width:1200px;height:459px;background:var(--footer)}
.foot-brand{left:83px;top:2305px;font-size:19px;font-weight:600;color:#1d2230}
.foot-text{left:83px;font-size:15px;line-height:19px;color:#2a2e38}
.foot-social{top:2444px;font-size:15px;font-weight:600;color:var(--navy)}
.foot-link{font-size:15px;color:#2a2e38;letter-spacing:.3px}
.foot-link.strong{font-weight:600;color:#111}
</style>
</head>
<body>

<header>
  <div class="abs brand-dot" aria-hidden="true"></div>
  <nav>
    <a class="abs nav-link" style="left:497px" href="#">Find a Mentor</a>
    <a class="abs nav-link" style="left:615px" href="#">For Businesses</a>
    <a class="abs nav-link" style="left:744px" href="#">Book a Sesion</a>
    <a class="abs btn-login" href="#">Login</a>
    <a class="abs btn-start" href="#">Get Started</a>
  </nav>
</header>

<section class="hero">
  <div class="abs avatar-lg" role="img" aria-label="Portrait photo of the mentor"></div>
  <span class="abs social" style="left:151px">Netlink</span>
  <span class="abs social" style="left:203px;color:#1da1f2">Chirp</span>
  <h1 class="abs mentor-name">Owen Carrow</h1>
  <p class="abs mentor-role">Director of Product - Harbor Cover</p>
  <div class="abs stars hero-stars">★★★★★</div>
  <span class="abs review-count">(4 Review)</span>
  <div class="abs price">$240/month</div>
  <a class="abs btn-apply" href="#">Apply for Mentorship</a>
  <span class="abs spots">3 Spot Available</span>
</section>

<main>
  <h2 class="abs section-title" style="left:109px;top:504px">Skill Taught by Mentor</h2>
  <div class="abs tags">
    <span class="tag active">Product Marketing</span>
    <span class="tag">Product</span>
    <span class="tag">Product manager</span>
    <span class="tag">Interview</span>
    <span class="tag">Startup</span>
    <span class="tag">Tech</span>
    <span class="tag">Media</span>
    <span class="tag">Technology</span>
    <span class="tag">Interview</span>
    <span class="tag">Pm</span>
    <span class="tag">Project manager</span>
    <span class="tag">Product management</span>
    <span class="tag">Interview prep</span>
    <span class="tag">Mock interview</span>
    <span class="tag">Product interview</span>
  </div>

  <h2 class="abs section-title" style="left:109px;top:745px">About</h2>
  <p class="abs para" style="top:785px">In 2013, I was among the most written-about founders, making waves at Northbeat Fest and The Evening Desk. After growing Loop Inc. to 6 million users organically and exited through acquisition by Tandem, I served as Chief Growth Officer at Wave9 Media, which I helped expand to Hong Kong, Malaysia, Singapore, Indonesia, Japan, and the US. Wave9 boasts over 60m users worldwide and runs the #1 livestreaming platform in Bridge Asia. I currently serve as an external Board Member for a Silicon Valley social company with over $200M in annual revenue.</p>
  <p class="abs para" style="top:925px">After growing startups in over 15 countries in Asia and the Americas, I have distilled a tried-and-true growth methods into the SMILE framework (Success, Metric, Ideas, Layout, Experiment). I specialize in Organic Growth with a Global Mindset, covering Global Growth, Product Growth, and Marketing Growth. You can find more at <a href="#">www.OwenCarrow.net</a>!</p>

  <h2 class="abs section-title" style="left:109px;top:1059px">What can I expect?</h2>
  <ul class="abs bullets">
    <li>•Unlimited access to the mentor via chat, e-mail or text, within reason.</li>
    <li>•You will have a 7 day trial for free with this mentor</li>
    <li>•Will give you tasks and exercises to complete, if wanted</li>
    <li>•Includes regular 1-on-1 calls, per agreement with mentor</li>
    <li>•Flat fee of $240 per month, no hidden costs</li>
  </ul>

  <h2 class="abs section-title" style="left:108px;top:1353px">Testimony</h2>

  <div class="abs testi-avatar" style="left:107px;top:1404px;background:linear-gradient(160deg,#7a9a6a,#c9403a)" role="img" aria-label="Photo of reviewer Milo"></div>
  <h3 class="abs testi-name" style="top:1404px;font-weight:400">Milo</h3>
  <div class="abs stars testi-stars" style="top:1430px">★★★★★</div>
  <p class="abs testi-text" style="top:1459px">Owen helped me set focus and intention in my goal of scaling my independent projects. Before working with Owen, I felt like I was jumping from idea to idea with no plan. During our session he provided clear action items which I enjoyed completing. Each week we reviewed the progress and established new items to iterate towards my goal. I am very thankful for my mentoring sessions with Owen.</p>

  <div class="abs testi-avatar" style="left:107px;top:1578px;background:linear-gradient(160deg,#c9d3e3,#44608f)" role="img" aria-label="Photo of reviewer Anton"></div>
  <h3 class="abs testi-name" style="top:1578px;font-weight:400">Anton</h3>
  <div class="abs stars testi-stars" style="top:1604px">★★★★★</div>
  <p class="abs testi-text" style="top:1632px">Owen is a great mentor, I feel that even just the couple of sessions we had provided me immense value. He came up with a number of tasks I should complete to get closer to my goals; tasks which he clearly explained and which were appropriate for the level of knowledge I had. The best part about the mentorship however was Owen's vast experience as a PM and the willingness to share it - learning from someone who has done what you want to do and who has battle-tested many different theories ultimately makes the most difference.</p>

  <a class="abs more-reviews" href="#">See more reviews</a>
</main>

<aside>
  <div class="abs card book-card"></div>
  <h2 class="abs section-title" style="left:810px;top:505px">Book a session</h2>

  <h3 class="abs session-name" style="top:574px">Work Review</h3>
  <p class="abs session-meta" style="top:598px">30 minutes, $69 per session</p>
  <a class="abs btn-book" style="top:634px" href="#">Book Session</a>
  <div class="abs divider" style="top:701px"></div>

  <h3 class="abs session-name" style="top:733px">Interview Preparation</h3>
  <p class="abs session-meta" style="top:757px">60 minutes, $99 per session</p>
  <a class="abs btn-book" style="top:794px" href="#">Book Session</a>
  <div class="abs divider" style="top:859px"></div>

  <h3 class="abs session-name" style="top:892px">Interview Preparation</h3>
  <p class="abs session-meta" style="top:916px">30 minutes, $69 per session</p>
  <a class="abs btn-book" style="top:953px" href="#">Book Session</a>

  <a class="abs btn-more" href="#">See more</a>

  <div class="abs card related-card"></div>
  <h2 class="abs section-title" style="left:810px;top:1188px">Related Mentors</h2>

  <div class="abs rel-avatar" style="top:1244px;background:linear-gradient(160deg,#6a3a3a,#3a2a4a)" role="img" aria-label="Photo of mentor Calvin Hart"></div>
  <h3 class="abs rel-name" style="top:1244px">Calvin Hart</h3>
  <p class="abs rel-role" style="top:1268px">The Global Growth Expert - CalvinHart.com</p>
  <p class="abs rel-price" style="top:1253px">$240<span>/month</span></p>

  <div class="abs rel-avatar" style="top:1339px;background:linear-gradient(160deg,#b7a9a3,#4a3530)" role="img" aria-label="Photo of mentor Dario Zane"></div>
  <h3 class="abs rel-name" style="top:1347px">Dario Zane</h3>
  <p class="abs rel-role" style="top:1372px;width:160px">Product Manager - Veranta</p>
  <p class="abs rel-price" style="top:1348px">$240<span>/month</span></p>

  <div class="abs rel-avatar" style="top:1434px;background:linear-gradient(160deg,#8fb0c9,#3a4f6a)" role="img" aria-label="Photo of mentor Calvin Hart"></div>
  <h3 class="abs rel-name" style="top:1436px">Calvin Hart</h3>
  <p class="abs rel-role" style="top:1460px;width:135px">Founder - Gloss and Code LLC</p>
  <p class="abs rel-price" style="top:1443px">$240<span>/month</span></p>

  <div class="abs rel-avatar" style="top:1530px;background:linear-gradient(160deg,#5a4a9a,#c9a33a)" role="img" aria-label="Photo of mentor Calvin Hart"></div>
  <h3 class="abs rel-name" style="top:1531px">Calvin Hart</h3>
  <p class="abs rel-role" style="top:1555px;width:120px">Technical Product Manager - Orchard</p>
  <p class="abs rel-price" style="top:1538px">$240<span>/month</span></p>
</aside>

<section>
  <div class="abs cta-band"></div>
  <h2 class="abs cta-heading">Ready to be mentored<br>by Owen Carrow</h2>
  <a class="abs btn-cta" href="#">Apply for Mentorship</a>
</section>

<footer>
  <div class="abs footer"></div>
  <div class="abs brand-dot" style="top:2258px" aria-hidden="true"></div>
  <div class="abs foot-brand">GuideHarbor</div>
  <p class="abs foot-text" style="top:2342px">Your trusted source to find highly-vetted mentors<br>&amp; industry professionals to move your career ahead.</p>
  <p class="abs foot-text" style="top:2397px">© 2020 GuideHarbor. All Rights Reserved.</p>
  <span class="abs foot-social" style="left:83px">Chirp</span>
  <span class="abs foot-social" style="left:133px">Friendbook</span>

  <a class="abs foot-link" style="left:613px;top:2343px" href="#">BROWSE MENTORS</a>
  <a class="abs foot-link" style="left:613px;top:2386px" href="#">BECOME A MENTORS</a>
  <a class="abs foot-link" style="left:613px;top:2429px" href="#">PARTNER PROGRAM</a>
  <a class="abs foot-link" style="left:613px;top:2473px" href="#">FAQ</a>
  <a class="abs foot-link" style="left:613px;top:2516px" href="#">BLOG</a>

  <a class="abs foot-link" style="left:878px;top:2343px" href="#">ABOUT US</a>
  <a class="abs foot-link" style="left:878px;top:2386px" href="#">CODE OF CONDUCT</a>
  <a class="abs foot-link" style="left:878px;top:2429px" href="#">PRIVACY POLICY</a>
  <a class="abs foot-link" style="left:878px;top:2473px" href="#">SUCCESS STORIES</a>
  <a class="abs foot-link strong" style="left:878px;top:2516px" href="#">INFO@GUIDEHARBOR.COM</a>
</footer>

</body>
</html>
```